Pool Builder Website Design in arizona

Our current site is located here: tidemoor.net

We are looking to give this a modern facelift. We will be cutting your design into a wordpress theme so we can utilize the CMS plateform backend.

Look and Feel
• Clean cut and professional
• Mobile friendly
• Updated from old site
• Feel intrigued but relax (do you have trust logos? Odile looking into this)
Colors
• Warm tropical neutral colors
• Orange, brown, blues
- Please make the site modern and more sleek look that looks like a 2015 style design and NOT 1999.
- Must be coded as a wordpress theme
- must create a home page, inner page and blog page
- must allow client to BLOG using the post section in wordpress

This pool company is a pool builder/installer in Phoenix arizona.

NOTE::: Please create a home page and one internal page.

Industry/Entity Type

Builder

Coding

Coded - Design and coding required

Number of Pages Required

3 page

Font styles to use
Serif
Sans Serif

Requirements
Must have
• - Must be coded as a wordpress theme
• - must create a home page, inner page and blog page
• - must allow client to BLOG using the post section in wordpress

```html
<!DOCTYPE html>
<html lang="en">
<head>
<meta charset="utf-8">
<title>Tidemoor Pools</title>
<link rel="stylesheet" href="https://fonts.googleapis.com/css2?family=Lato:wght@300;400;700&display=swap">
<style>
:root{
  --blue:#2f8fd6;
  --blue-light:#5bb8e4;
  --btn:#5bbde2;
  --ink:#2b2b2b;
  --text:#777;
  --muted:#999;
  --nav-bg:#f3f3f3;
  --line:#d8d8d8;
  --white:#fff;
}
*{box-sizing:border-box;margin:0;padding:0}
html,body{width:1200px;height:2449px;overflow:hidden;background:var(--white);font-family:'Lato',Arial,sans-serif;color:var(--text)}
.wrap{width:1028px;margin:0 auto;position:relative}

.top-bar{height:68px}
.top-bar .wrap{display:flex;justify-content:space-between;align-items:center;height:68px}
.brand{font-size:34px;font-weight:400;color:var(--blue);letter-spacing:.3px}
.follow{display:flex;align-items:center;gap:5px;font-size:13px;color:var(--ink)}
.follow span{margin-right:4px}
.social-square{width:24px;height:24px;background:#8a98a8}

.main-nav{height:38px;background:var(--nav-bg);border-top:1px solid #e4e4e4;border-bottom:1px solid #e4e4e4}
.main-nav .wrap{display:flex;align-items:center;height:36px}
.main-nav a{font-size:13px;color:var(--ink);text-decoration:none;margin-right:62px}
.search{margin-left:auto;width:240px;height:24px;background:var(--white);border:1px solid #ddd;font-size:11px;color:#aaa;padding:5px 8px;display:flex;justify-content:space-between;align-items:center}

.hero{height:389px;background:linear-gradient(180deg,#b9dbef 0%,#6fb8e2 38%,#2f8fcf 60%,#59b6e6 82%,#cfe8f5 100%)}

.welcome{height:270px;text-align:center;padding-top:32px}
.welcome h1{font-size:27px;font-weight:400;color:var(--ink)}
.welcome h1 strong{font-size:40px;font-weight:400;color:var(--blue)}
.welcome h2{font-size:25px;font-weight:700;color:var(--blue-light);margin-top:0}
.welcome p{width:880px;margin:22px auto 0;font-size:13px;line-height:24px;color:var(--text)}
.btn{display:inline-block;background:var(--btn);color:var(--white);font-size:12px;font-weight:700;letter-spacing:.5px;border-radius:3px;text-decoration:none}
.welcome .btn{margin-top:20px;width:142px;height:42px;line-height:42px}

.gallery-title{display:flex;align-items:center;gap:24px;margin-top:20px}
.gallery-title::before,.gallery-title::after{content:"";flex:1;height:1px;background:var(--line)}
.gallery-title h3{font-size:29px;font-weight:400;color:var(--ink)}
.gallery-grid{display:grid;grid-template-columns:repeat(4,242px);gap:18px 20px;margin-top:36px}
.tile{height:256px}

.info{display:flex;margin-top:40px;height:235px}
.who{width:520px;padding-right:40px;border-right:1px solid var(--line)}
.info h4{font-size:23px;font-weight:400;color:var(--ink)}
.who p{margin-top:18px;font-size:12px;line-height:24px;color:var(--muted)}
.who .btn{margin-top:24px;width:142px;height:42px;line-height:42px;text-align:center}
.news{padding-left:42px;flex:1}
.news-item{display:flex;gap:18px;margin-top:26px}
.news-item + .news-item{margin-top:16px}
.thumb{width:92px;height:76px;flex:none;border:3px solid #e9e9e9}
.news-item h5{font-size:12px;font-weight:700;color:var(--blue-light)}
.news-item p{font-size:12px;line-height:20px;color:var(--muted);margin-top:4px}
.news-item a{font-size:11px;color:var(--blue-light);text-decoration:none}

.signup{height:322px;margin-top:33px;background:linear-gradient(180deg,#3b4a55 0%,#56656c 45%,#6b6a5e 70%,#3a3a34 100%);text-align:center;padding-top:66px;color:var(--white)}
.signup h3{font-size:33px;font-weight:700;letter-spacing:.5px}
.signup p{font-size:18px;margin-top:2px}
.signup form{display:flex;justify-content:center;gap:10px;margin-top:48px}
.field{width:187px;height:36px;background:rgba(210,215,220,.35);border:1px solid rgba(255,255,255,.3);color:var(--white);font-size:12px;text-align:left;padding:10px 12px}
.submit{width:78px;height:36px;background:var(--blue);color:var(--white);font-size:12px;font-weight:700;line-height:36px}

.map{height:258px;margin-top:5px;background:linear-gradient(160deg,#eef0ec 0%,#e3e6e0 60%,#dfe3e6 100%)}

.footer{height:186px}
.footer .cols{display:flex;width:740px;margin:0 auto;padding-top:30px;gap:0}
.footer .col{width:300px}
.footer h6{font-size:16px;font-weight:400;color:var(--ink)}
.footer .col p{font-size:12px;line-height:18px;color:var(--text);margin-top:10px}
.footer .col:last-child{margin-left:0}
.footer .copy{width:780px;margin:36px auto 0;border-top:1px solid var(--line);padding-top:12px;text-align:center;font-size:11px;color:var(--text)}
</style>
</head>
<body>

<header class="top-bar">
  <div class="wrap">
    <div class="brand">Tidemoor Pools</div>
    <div class="follow"><span>Follow Us :</span><i class="social-square"></i><i class="social-square"></i><i class="social-square"></i><i class="social-square"></i></div>
  </div>
</header>

<nav class="main-nav">
  <div class="wrap">
    <a href="#">Home</a><a href="#">About Us</a><a href="#">Styles</a><a href="#">Portfolio</a><a href="#">Installation</a><a href="#">Contact Us</a>
    <div class="search">Search
      <svg width="12" height="12" viewBox="0 0 12 12"><circle cx="5" cy="5" r="3.6" fill="none" stroke="#aaa" stroke-width="1.3"/><line x1="7.7" y1="7.7" x2="11" y2="11" stroke="#aaa" stroke-width="1.3"/></svg>
    </div>
  </div>
</nav>

<section class="hero" role="img" aria-label="Sparkling blue swimming pool with steel ladder under a bright sky"></section>

<section class="welcome">
  <h1>Welcome to <strong>Tidemoor Pools</strong></h1>
  <h2>the Fiberglass Pool Experts!</h2>
  <p>A Phoenix Fiberglass pool is more than just a relaxing piece of leisure, it is an investment. Why spend your money on a pool that requires more maintenance and scratches your feet when you can enjoy the smooth feeling of fiberglass on your toes? Fiberglass pools offer many unique advantages over concrete pools, and Tidemoor Pools are the premier AZ fiberglass pool builders.</p>
  <a class="btn" href="#">READ MORE</a>
</section>

<section class="wrap gallery">
  <div class="gallery-title"><h3>Our Gallery</h3></div>
  <div class="gallery-grid">
    <div class="tile" role="img" aria-label="Backyard pool with spa" style="background:linear-gradient(160deg,#9fd3ea,#3aa0d0)"></div>
    <div class="tile" role="img" aria-label="Seaside city skyline over the bay" style="background:linear-gradient(180deg,#cfe3f2,#8fb1c8 55%,#2e6f9e)"></div>
    <div class="tile" role="img" aria-label="Resort pool with palm trees" style="background:linear-gradient(180deg,#7ab6e0,#5c7d64 45%,#3a9dcf)"></div>
    <div class="tile" role="img" aria-label="Pool ladder over clear water" style="background:linear-gradient(160deg,#bfe6f5,#1f8ccd)"></div>
    <div class="tile" role="img" aria-label="Poolside loungers under an umbrella" style="background:linear-gradient(180deg,#4f9ee0,#9bd0ee 55%,#c6a878)"></div>
    <div class="tile" role="img" aria-label="Pool in a garden setting" style="background:linear-gradient(180deg,#2f4a36,#4a8f9e 55%,#2d7fb2)"></div>
    <div class="tile" role="img" aria-label="Pool with handrail beside a house" style="background:linear-gradient(180deg,#c9b89a,#6fbde6 45%,#2e95d6)"></div>
    <div class="tile" role="img" aria-label="Above-ground pool with ladder" style="background:linear-gradient(180deg,#b8bcc0,#e5e7e8 40%,#3fa6e0)"></div>
  </div>

  <div class="info">
    <div class="who">
      <h4>Who We Are?</h4>
      <p>Tidemoor Pools was founded for one simple reason, to make a better pools. We are family owned and operated, and Tidemoor Pools has been serving the valley for years. Chances are if you are in AZ and you step into a pool that feels extraordinarily smooth, Tidemoor Pools was responsible for it. The difference is fiberglass.</p>
      <a class="btn" href="#">READ MORE</a>
    </div>
    <div class="news">
      <h4>Latest News</h4>
      <div class="news-item">
        <div class="thumb" role="img" aria-label="Resort pool" style="background:linear-gradient(180deg,#7a6a55,#3f95c8)"></div>
        <div><h5>Lorem Ipsum</h5><p>Lorem Ipsum is simply dummy text of the printing and typesetting industry. Lorem Ipsum has been.</p><a href="#">Read More</a></div>
      </div>
      <div class="news-item">
        <div class="thumb" role="img" aria-label="Poolside umbrella" style="background:linear-gradient(180deg,#5aa6e2,#b89a6c)"></div>
        <div><h5>Lorem Ipsum</h5><p>Lorem Ipsum is simply dummy text of the printing and typesetting industry. Lorem Ipsum has been.</p><a href="#">Read More</a></div>
      </div>
    </div>
  </div>
</section>

<section class="signup" role="img" aria-label="Beach at dusk with boats and a thatched shelter">
  <h3>SIGN UP BELOW TO GET UPDATES!</h3>
  <p>Lorem Ipsum is simply dummy text</p>
  <form>
    <div class="field">Your Name</div>
    <div class="field">Your Email</div>
    <div class="submit">Submit</div>
  </form>
</section>

<section class="map" role="img" aria-label="Street map showing the office location"></section>

<footer class="footer">
  <div class="cols">
    <div class="col">
      <h6>Tidemoor Pools</h6>
      <p>1870 W Palo Verde Rd,<br>Phoenix, AZ 85021</p>
    </div>
    <div class="col">
      <h6>Call Now! 602-555-0148</h6>
      <p>Toll Free 1-800-555-0172<br>Fax 602-555-0149</p>
    </div>
  </div>
  <div class="copy">copyright © Tidemoor Pools 2015,all rights reserved</div>
</footer>

</body>
</html>
```